Korvanta Business Card

Looking for business card ideas. Company name is Korvanta. Have a few basic ideas on attachment. Please submit anything with the logo and general information from attachment.

Industry/Entity Type

Business

```html
<!DOCTYPE html>
<html lang="en">
<head>
<meta charset="utf-8">
<title>Korvanta Business Card</title>
<link rel="stylesheet" href="https://fonts.googleapis.com/css2?family=Lato:wght@400;700&display=swap">
<style>
  :root {
    --backdrop: #c4c4c4;
    --card-black: #050505;
    --card-white: #f7f7f7;
    --brand-red: #d81a1a;
    --ink: #111111;
    --divider: #000000;
  }
  html, body {
    margin: 0;
    padding: 0;
    width: 1200px;
    height: 960px;
    overflow: hidden;
    background: var(--backdrop);
    font-family: "Lato", sans-serif;
  }
  .stage {
    width: 1200px;
    height: 960px;
    display: flex;
    align-items: center;
    justify-content: center;
  }
  .card {
    display: flex;
    width: 1060px;
    height: 600px;
    box-shadow: 0 18px 40px rgba(0,0,0,0.25);
  }
  .card-front {
    width: 520px;
    height: 100%;
    background: var(--card-black);
    position: relative;
  }
  .brand {
    position: absolute;
    left: 0;
    right: 0;
    top: 170px;
    display: flex;
    flex-direction: column;
    align-items: center;
    gap: 34px;
  }
  .brand-dot {
    width: 150px;
    height: 150px;
    border-radius: 50%;
    background: var(--brand-red);
  }
  .brand-name {
    font-size: 64px;
    font-weight: 700;
    color: var(--brand-red);
    letter-spacing: 4px;
  }
  .card-divider {
    width: 14px;
    height: 100%;
    background: var(--card-white);
    display: flex;
    justify-content: center;
  }
  .card-divider span {
    width: 6px;
    height: 100%;
    background: var(--divider);
  }
  .card-back {
    flex: 1;
    height: 100%;
    background: linear-gradient(180deg, #ffffff, #ececec);
    padding: 170px 0 0 110px;
    box-sizing: border-box;
  }
  .person-name {
    font-size: 40px;
    font-weight: 400;
    color: var(--brand-red);
    margin: 0;
    line-height: 1.1;
  }
  .person-role {
    font-size: 24px;
    font-weight: 700;
    color: var(--ink);
    margin: 2px 0 36px;
  }
  .contact-list {
    list-style: none;
    margin: 0;
    padding: 0;
  }
  .contact-item {
    display: flex;
    align-items: flex-start;
    gap: 18px;
    font-size: 22px;
    color: var(--ink);
    line-height: 1.2;
    margin-bottom: 12px;
  }
  .contact-icon {
    width: 20px;
    height: 20px;
    flex: none;
    margin-top: 3px;
    fill: var(--brand-red);
  }
</style>
</head>
<body>
<main class="stage">
  <article class="card">
    <section class="card-front">
      <div class="brand">
        <div class="brand-dot"></div>
        <div class="brand-name">Korvanta</div>
      </div>
    </section>
    <div class="card-divider"><span></span></div>
    <section class="card-back">
      <h1 class="person-name">Dale Mercer</h1>
      <p class="person-role">Director</p>
      <ul class="contact-list">
        <li class="contact-item">
          <svg class="contact-icon" viewBox="0 0 20 20" aria-hidden="true"><path d="M3 2h14v18h-5v-4H8v4H3zM6 5v2h2V5zm6 0v2h2V5zM6 9v2h2V9zm6 0v2h2V9z"/></svg>
          <span>(555) 010-4820</span>
        </li>
        <li class="contact-item">
          <svg class="contact-icon" viewBox="0 0 20 20" aria-hidden="true"><path d="M5 1l3 1 1 4-2 2c1 2 3 4 5 5l2-2 4 1 1 3-2 3C9 18 2 11 2 4z"/></svg>
          <span>(555) 010-7364</span>
        </li>
        <li class="contact-item">
          <svg class="contact-icon" viewBox="0 0 20 20" aria-hidden="true"><path d="M10 1a9 9 0 100 18 9 9 0 000-18zm0 2c.9 1.3 1.6 3 1.9 5H8.1C8.4 6 9.1 4.3 10 3zM3.2 8H6a15 15 0 000 4H3.2a7 7 0 010-4zm4.9 0h3.8a13 13 0 010 4H8.1a13 13 0 010-4zM14 8h2.8a7 7 0 010 4H14a15 15 0 000-4zm-5.9 6h3.8c-.3 2-1 3.7-1.9 5-.9-1.3-1.6-3-1.9-5z"/></svg>
          <span>www.korvanta.org</span>
        </li>
        <li class="contact-item">
          <svg class="contact-icon" viewBox="0 0 20 20" aria-hidden="true"><path d="M1 4h18v12H1zm2 2v.5l7 5 7-5V6l-7 5z"/></svg>
          <span>dmercer@halvrix.com</span>
        </li>
        <li class="contact-item">
          <svg class="contact-icon" viewBox="0 0 20 20" aria-hidden="true"><path d="M10 1l9 8h-3v10h-4v-6H8v6H4V9H1z"/></svg>
          <span>2408 W. Larkspur Ave Brenton,<br>TX 75521</span>
        </li>
      </ul>
    </section>
  </article>
</main>
</body>
</html>
```